letterhead design for a investing company*

Design an appealing business letterhead to match with our existing logo and attract new customers. Our customers are mainly corporate managers which are detail oriented and judge the company ability to perform a good service based on small details. A professional letterhead will give a good first impression.

Target Market(s)

New customers and business owners

Industry/Entity Type

Marketplace

Font styles to use
Sans Serif
Script

Requirements
Must have
• Must be a professional and elegant design that attracts interest from people who receives it

```html
<!DOCTYPE html>
<html lang="en">
<head>
<meta charset="utf-8">
<title>Brightwell Stationery</title>
<link rel="stylesheet" href="https://fonts.googleapis.com/css2?family=Open+Sans:wght@400;600;700&display=swap">
<style>
  :root {
    --bg: #ececee;
    --paper: #ffffff;
    --navy: #14203f;
    --gold: #f0ab1c;
    --text: #8b8b8e;
    --faint: #eeeff1;
  }
  * { box-sizing: border-box; margin: 0; padding: 0; }
  html, body { width: 1200px; height: 1128px; overflow: hidden; }
  body {
    background: var(--bg);
    font-family: "Open Sans", Arial, sans-serif;
    position: relative;
  }
  .letterhead {
    position: absolute; left: 40px; top: 40px;
    width: 742px; height: 1048px;
    background: var(--paper);
    box-shadow: 0 6px 22px rgba(0,0,0,.08);
  }
  .brand {
    position: absolute; left: 60px; top: 56px;
    display: flex; align-items: center; gap: 10px;
  }
  .brand-dot { width: 18px; height: 18px; border-radius: 50%; background: var(--gold); }
  .brand-name { font-size: 30px; font-weight: 700; color: var(--navy); letter-spacing: .5px; }
  .letter-body {
    position: absolute; left: 60px; top: 150px; width: 620px;
    color: var(--text); font-size: 12.5px; line-height: 1.45;
  }
  .greeting { margin-bottom: 16px; }
  .letter-body p { margin-bottom: 14px; }
  .closing { margin-top: 18px; }
  .signature {
    width: 110px; height: 70px; margin-top: 14px;
    background: linear-gradient(135deg, #f2f2f3, #e4e4e6);
    border-radius: 4px;
  }
  .contact {
    position: absolute; left: 60px; bottom: 100px;
    color: var(--navy); font-size: 13px; line-height: 1.7;
  }
  .contact li { list-style: none; display: flex; align-items: center; gap: 8px; }
  .contact svg { width: 13px; height: 13px; fill: var(--gold); flex: none; }
  .address {
    position: absolute; left: 300px; bottom: 82px;
    color: var(--navy); font-size: 13px; line-height: 1.55;
  }
  .address strong { font-weight: 600; }
  .mascot-watermark {
    position: absolute; right: 40px; bottom: 30px;
    width: 210px; height: 250px; border-radius: 40% 40% 10px 10px;
    background: linear-gradient(180deg, var(--faint), #f7f7f8);
  }
  .card {
    position: absolute; width: 250px; height: 390px;
    background: var(--paper);
    box-shadow: 0 5px 16px rgba(0,0,0,.08);
    display: flex; align-items: center; justify-content: center;
  }
  .card-front { left: 880px; top: 110px; }
  .card-back { left: 880px; top: 580px; }
  .card .brand { position: static; gap: 7px; }
  .card .brand-name { font-size: 22px; }
  .card .brand-dot { width: 13px; height: 13px; }
  .card-mascot {
    width: 150px; height: 210px; border-radius: 45% 45% 12px 12px;
    background: linear-gradient(180deg, #22305a, var(--navy));
  }
</style>
</head>
<body>
  <section class="letterhead">
    <div class="brand"><span class="brand-dot"></span><span class="brand-name">Brightwell</span></div>

    <div class="letter-body">
      <div class="greeting">Dear customer,</div>
      <p>Lorem ipsum dolor sit amet, consectetur adipisicing elit, sed do eiusmod tempor incididunt ut labore et dolore magna aliqua. Ut enim ad minim veniam, quis nostrud exercitation ullamco laboris nisi ut aliquip ex ea commodo consequat. Duis aute irure dolor in reprehenderit in voluptate velit esse cillum dolore eu fugiat nulla pariatur. Excepteur sint occaecat cupidatat non proident, sunt in culpa qui officia deserunt mollit anim id est laborum.</p>
      <p>Lorem ipsum dolor sit amet, consectetur adipisicing elit, sed do eiusmod tempor incididunt ut labore et dolore magna aliqua. Ut enim ad minim veniam, quis nostrud exercitation ullamco laboris nisi ut aliquip ex ea commodo consequat. Duis aute irure dolor in reprehenderit in voluptate velit esse cillum dolore eu fugiat nulla pariatur. Excepteur sint occaecat cupidatat non proident, sunt in culpa qui officia deserunt mollit anim id est laborum.</p>
      <p>Lorem ipsum dolor sit amet, consectetur adipisicing elit, sed do eiusmod tempor incididunt ut labore et dolore magna aliqua. Ut enim ad minim veniam, quis nostrud exercitation ullamco laboris nisi ut aliquip ex ea commodo consequat. Duis aute irure dolor in reprehenderit in voluptate velit esse cillum dolore eu fugiat nulla pariatur. Excepteur sint occaecat cupidatat non proident, sunt in culpa qui officia deserunt mollit anim id est laborum.</p>
      <p>Lorem ipsum dolor sit amet, consectetur adipisicing elit, sed do eiusmod tempor incididunt ut labore et dolore magna aliqua. Ut enim ad minim veniam, quis nostrud exercitation ullamco laboris nisi ut aliquip ex ea commodo consequat. Duis aute irure dolor in reprehenderit.</p>
      <div class="closing">Yours Sincerely,</div>
      <div class="signature" role="img" aria-label="Handwritten signature"></div>
    </div>

    <ul class="contact">
      <li><svg viewBox="0 0 16 16"><path d="M3 1h3l1.5 4-2 1.3a9 9 0 0 0 4.2 4.2L11 8.5l4 1.5v3a2 2 0 0 1-2 2A12 12 0 0 1 1 3a2 2 0 0 1 2-2z"/></svg>555.214.0187</li>
      <li><svg viewBox="0 0 16 16"><path d="M1 3h14v10H1z M1 3l7 6 7-6" fill="none" stroke="#f0ab1c" stroke-width="1.6"/></svg>info@brightwell.example</li>
      <li><svg viewBox="0 0 16 16"><circle cx="8" cy="8" r="7"/></svg>www.brightwell.example</li>
    </ul>

    <address class="address" style="font-style:normal">
      <strong>Brightwell Ltd.</strong><br>
      48 Harbour Lane,<br>
      Westbury, ON K2P 4R7
    </address>

    <div class="mascot-watermark" role="img" aria-label="Faint mascot character giving a thumbs up"></div>
  </section>

  <section class="card card-front">
    <div class="brand"><span class="brand-dot"></span><span class="brand-name">Brightwell</span></div>
  </section>

  <section class="card card-back">
    <div class="card-mascot" role="img" aria-label="Navy mascot character giving a thumbs up"></div>
  </section>
</body>
</html>
```